Business Card design which attached logo. Company is called Tailored Shield and main colours are Orange & Black.

Company specialises in Paint Protection and Detailing for supercars.

Details needed on business card:

Sales

Address: Unit 14, 227 Harlow Street, Fernmere Vale, NSW 2391

Phone: 02 8419 2753

website: www.tailoredshield.com.au

Email: sales@tailoredshield.com.au

```html
<!DOCTYPE html>
<html lang="en">
<head>
<meta charset="utf-8">
<title>Tailored Shield – Business Card</title>
<link href="https://fonts.googleapis.com/css2?family=Roboto:wght@300;400;500&display=swap" rel="stylesheet">
<style>
  :root {
    --ink: #141414;
    --orange: #ef5a24;
    --backdrop: #e9e9e9;
  }
  * { box-sizing: border-box; margin: 0; padding: 0; }
  html, body {
    width: 1200px; height: 800px; overflow: hidden;
    background: var(--backdrop);
    font-family: "Roboto", Arial, sans-serif;
  }
  .canvas {
    position: relative; width: 1200px; height: 800px;
    display: flex; align-items: center; justify-content: center; gap: 60px;
  }
  .card {
    position: relative; width: 520px; height: 297px;
    background: var(--ink); overflow: hidden;
    box-shadow: 0 10px 30px rgba(0,0,0,.18);
  }
  .card-frame { position: absolute; inset: 0; }

  /* front */
  .company-name {
    position: absolute; left: 30px; top: 72px;
    color: var(--orange); font-weight: 400; font-size: 27px; letter-spacing: .5px;
    text-transform: uppercase;
  }
  .name-rule {
    position: absolute; left: 32px; top: 108px; width: 60px; height: 7px;
    background: var(--orange);
  }
  .contact-list {
    position: absolute; left: 40px; top: 132px; list-style: none;
    color: var(--orange); font-size: 13.5px; line-height: 1.25;
  }
  .contact-item { display: flex; align-items: flex-start; gap: 10px; margin-bottom: 6px; }
  .contact-icon { width: 13px; height: 13px; flex: none; margin-top: 2px; fill: var(--orange); }
  .vehicle-art {
    position: absolute; right: 24px; top: 62px; width: 170px; height: 160px;
    background: radial-gradient(ellipse at center, rgba(239,90,36,.35), rgba(239,90,36,0) 70%);
  }

  /* back */
  .accent-band {
    position: absolute; left: 0; right: 0; top: 172px; height: 62px;
    background: var(--orange);
  }
  .vehicle-art--back {
    position: absolute; left: 150px; top: 28px; width: 230px; height: 150px;
    background: radial-gradient(ellipse at center, rgba(239,90,36,.35), rgba(239,90,36,0) 70%);
  }
  .brand-mark {
    position: absolute; left: 0; right: 0; top: 186px; text-align: center;
    color: var(--ink); font-weight: 300; font-size: 26px; letter-spacing: 1px;
    text-transform: uppercase;
  }
</style>
</head>
<body>
<main class="canvas">

  <section class="card card--front" aria-label="Card front">
    <svg class="card-frame" viewBox="0 0 520 297" fill="none" stroke="var(--orange)" stroke-width="1.5">
      <path d="M0 40 H110 L120 52 H300 L310 40 H520"/>
      <path d="M0 268 H60 L72 250 H290 L302 236 H520"/>
    </svg>
    <h1 class="company-name">Tailored Shield</h1>
    <div class="name-rule" role="img" aria-label="Striped accent under the name"></div>
    <ul class="contact-list">
      <li class="contact-item">
        <svg class="contact-icon" viewBox="0 0 24 24"><path d="M12 2a7 7 0 0 0-7 7c0 5 7 13 7 13s7-8 7-13a7 7 0 0 0-7-7zm0 9.5A2.5 2.5 0 1 1 12 6.5a2.5 2.5 0 0 1 0 5z"/></svg>
        <span>Unit 14, 227 Harlow Street<br>Fernmere Vale, NSW 2391</span>
      </li>
      <li class="contact-item">
        <svg class="contact-icon" viewBox="0 0 24 24"><path d="M6.6 10.8a15 15 0 0 0 6.6 6.6l2.2-2.2a1 1 0 0 1 1-.25 11.4 11.4 0 0 0 3.6.6 1 1 0 0 1 1 1V20a1 1 0 0 1-1 1A17 17 0 0 1 3 4a1 1 0 0 1 1-1h3.5a1 1 0 0 1 1 1c0 1.25.2 2.45.6 3.6a1 1 0 0 1-.25 1z"/></svg>
        <span>02 8419 2753</span>
      </li>
      <li class="contact-item">
        <svg class="contact-icon" viewBox="0 0 24 24" fill="none" stroke="var(--orange)" stroke-width="2.5"><circle cx="12" cy="12" r="4"/><path d="M16 8v5a3 3 0 0 0 6 0v-1a10 10 0 1 0-4 8"/></svg>
        <span>sales@tailoredshield.com.au</span>
      </li>
      <li class="contact-item">
        <svg class="contact-icon" viewBox="0 0 24 24" fill="none" stroke="var(--orange)" stroke-width="2"><circle cx="12" cy="12" r="10"/><path d="M2 12h20M12 2c3 3 3 17 0 20M12 2c-3 3-3 17 0 20"/></svg>
        <span>www.tailoredshield.com.au</span>
      </li>
    </ul>
    <div class="vehicle-art" role="img" aria-label="Orange line drawing of a supercar in side view"></div>
  </section>

  <section class="card card--back" aria-label="Card back">
    <div class="accent-band"></div>
    <div class="vehicle-art--back" role="img" aria-label="Orange line drawing of a supercar in side view"></div>
    <p class="brand-mark">Tailored Shield</p>
  </section>

</main>
</body>
</html>
```